8x8 Social Media Ad - Harbor Summit Expo

Attention Real Estate Agents
Please join us for our
Quarterly Real Estate Training Expo
The 2nd Saturday of February, May, August and November
Our Next Training Expo is _________________________________
From 9 am to 1 pm
at
Marlowe Suites Fernridge Station
4187 Copperleaf Lane, Greenbelt, MD 20770
Scheduled Speakers
9:00 am - Desmond Pryce - Orientation
9:30 am - Terrell Oakes - Multiple Income Streams / Keystone Track
10:00 am - Lorna Beckett - Marketing though Social Media
10:45 am - Raul Denning - Generating Business through Kelp-Nest
11:30 am - Tunde Adesemi - Real Estate Investing
12:15 pm - Marcus Oyelowo - (Main Speaker) Training Topic TBA
For more information call Desmond Pryce at (240) 555-0192 or email dpryce@harborsummithomes.example

```html
<!DOCTYPE html>
<html lang="en">
<head>
<meta charset="utf-8">
<title>Harbor Summit Expo – Quarterly Real Estate Training Expo</title>
<link rel="stylesheet" href="https://fonts.googleapis.com/css2?family=Signika:wght@400;500;600;700&display=swap">
<style>
  :root {
    --teal: #129a8a;
    --ink: #262626;
    --paper: #ffffff;
    --photo-light: #eef0f1;
    --photo-mid: #b9bec2;
    --photo-dark: #6b7278;
  }
  html, body {
    margin: 0;
    width: 1200px;
    height: 1200px;
    overflow: hidden;
    background: var(--paper);
  }
  .ad {
    display: block;
    width: 1200px;
    height: 1200px;
    font-family: "Signika", sans-serif;
  }
  .fill-teal { fill: var(--teal); }
  .fill-ink { fill: var(--ink); }
  .fill-paper { fill: var(--paper); }
  .brand-name { fill: var(--teal); font-weight: 600; }
  .headline { fill: var(--teal); font-weight: 700; font-size: 64px; }
  .invite { fill: var(--paper); font-weight: 600; font-size: 46px; }
  .details { fill: var(--paper); font-weight: 500; font-size: 30px; }
  .venue { fill: var(--paper); font-weight: 700; font-size: 30px; }
  .date-line { stroke: var(--paper); stroke-width: 2.5; }
  .speakers-title { fill: var(--paper); font-weight: 700; font-size: 39px; }
  .slot-time { fill: var(--teal); font-weight: 700; font-size: 26px; }
  .slot-talk { fill: var(--paper); font-weight: 500; font-size: 17px; }
  .contact { fill: var(--paper); font-weight: 600; font-size: 27px; }
  .contact-small { fill: var(--paper); font-weight: 500; font-size: 25px; }
  .speaker-ring { fill: none; stroke: var(--paper); stroke-width: 2; stroke-dasharray: 6 4; }
  .speaker-photo { fill: url(#speakerTone); }
</style>
</head>
<body>
<svg class="ad" viewBox="206 206 1520 1520" xmlns="http://www.w3.org/2000/svg">
  <defs>
    <linearGradient id="photoTone" x1="0" y1="0" x2="1" y2="1">
      <stop offset="0" stop-color="#d9dcde"/>
      <stop offset="0.45" stop-color="#9fb5c6"/>
      <stop offset="1" stop-color="#f2f2f2"/>
    </linearGradient>
    <linearGradient id="photoFade" x1="0" y1="0" x2="0" y2="1">
      <stop offset="0" stop-color="#ffffff" stop-opacity="1"/>
      <stop offset="0.08" stop-color="#ffffff" stop-opacity="0"/>
      <stop offset="0.88" stop-color="#ffffff" stop-opacity="0"/>
      <stop offset="1" stop-color="#ffffff" stop-opacity="1"/>
    </linearGradient>
    <linearGradient id="speakerTone" x1="0" y1="0" x2="0" y2="1">
      <stop offset="0" stop-color="#c9c3bd"/>
      <stop offset="1" stop-color="#5d5651"/>
    </linearGradient>
  </defs>

  <!-- base -->
  <rect class="fill-paper" x="206" y="206" width="1520" height="1520"/>

  <!-- brand name -->
  <g class="brand">
    <rect class="fill-teal" x="272" y="285" width="34" height="34"/>
    <text class="brand-name" x="318" y="318" font-size="44">HARBOR SUMMIT</text>
    <text class="brand-name" x="272" y="372" font-size="28">REALTY GROUP</text>
  </g>

  <!-- hero photo area -->
  <g class="hero-photo" role="img" aria-label="Photo of a young real estate agent in glasses and a denim shirt writing notes at a desk">
    <rect x="206" y="470" width="760" height="870" fill="url(#photoTone)"/>
    <rect x="206" y="470" width="760" height="870" fill="url(#photoFade)"/>
  </g>

  <!-- top-right stripes -->
  <polygon class="fill-ink" points="1340,206 1415,206 1275,490 1200,490"/>
  <polygon class="fill-teal" points="1420,206 1685,206 1540,490 1275,490"/>
  <polygon class="fill-ink" points="1685,206 1726,206 1726,230 1615,490 1540,490"/>

  <!-- main teal panel -->
  <polygon class="fill-teal" points="1080,493 1726,493 1726,1726 640,1726 945,1130 745,1128"/>
  <!-- dark speaker panel -->
  <polygon class="fill-ink" points="1175,1125 1726,1125 1726,1726 905,1726"/>
  <!-- dark diagonal stripe -->
  <polygon class="fill-ink" points="905,1130 945,1130 640,1726 600,1726"/>

  <!-- contact band -->
  <polygon class="fill-teal" points="206,1493 693,1493 760,1377 780,1377 632,1660 206,1660"/>

  <!-- headline -->
  <text class="headline" x="912" y="322">ATTENTION</text>
  <text class="headline" x="823" y="386">REAL ESTATE</text>
  <text class="headline" x="937" y="449">AGENTS</text>

  <!-- invitation -->
  <text class="invite" x="1080" y="585">PLEASE JOIN US FOR OUR</text>
  <text class="invite" x="1045" y="660">QUARTERLY REAL ESTATE</text>
  <text class="invite" x="1022" y="717">TRAINING EXPO</text>

  <text class="details" x="963" y="783">THE 2ND SATURDAY OF FEBRUARY, MAY, AUGUST</text>
  <text class="details" x="935" y="823">AND NOVEMBER</text>
  <text class="details" x="912" y="865">OUR NEXT TRAINING EXPO IS</text>
  <line class="date-line" x1="1337" y1="868" x2="1672" y2="868"/>
  <text class="details" x="884" y="917">FROM 9 AM TO 1 PM @</text>
  <text class="venue" x="862" y="960">MARLOWE SUITES FERNRIDGE STATION</text>
  <text class="venue" x="836" y="1003">4187 COPPERLEAF LANE, GREENBELT, MD 20770</text>

  <!-- speaker portraits -->
  <g class="speaker" role="img" aria-label="Portrait of speaker Lorna Beckett">
    <circle class="speaker-photo" cx="1202" cy="1127" r="70"/>
    <circle class="speaker-ring" cx="1202" cy="1127" r="77"/>
  </g>
  <g class="speaker" role="img" aria-label="Portrait of speaker Terrell Oakes">
    <circle class="speaker-photo" cx="1405" cy="1125" r="70"/>
    <circle class="speaker-ring" cx="1405" cy="1125" r="79"/>
  </g>
  <g class="speaker" role="img" aria-label="Portrait of speaker Marcus Oyelowo">
    <circle class="speaker-photo" cx="1608" cy="1127" r="72"/>
    <circle class="speaker-ring" cx="1608" cy="1127" r="80"/>
  </g>
  <g class="speaker" role="img" aria-label="Portrait of speaker Desmond Pryce">
    <circle class="speaker-photo" cx="1115" cy="1297" r="72"/>
    <circle class="speaker-ring" cx="1115" cy="1297" r="80"/>
  </g>
  <g class="speaker" role="img" aria-label="Portrait of speaker Raul Denning">
    <circle class="speaker-photo" cx="1032" cy="1462" r="70"/>
    <circle class="speaker-ring" cx="1032" cy="1462" r="77"/>
  </g>
  <g class="speaker" role="img" aria-label="Portrait of speaker Tunde Adesemi">
    <circle class="speaker-photo" cx="948" cy="1620" r="70"/>
    <circle class="speaker-ring" cx="948" cy="1620" r="77"/>
  </g>

  <!-- schedule -->
  <g class="schedule" text-anchor="end">
    <text class="speakers-title" x="1662" y="1266">SCHEDULED SPEAKERS</text>

    <text class="slot-time" x="1662" y="1314">9:00 am</text>
    <text class="slot-talk" x="1662" y="1336">Desmond Pryce - Orientation</text>

    <text class="slot-time" x="1662" y="1379">9:30 am</text>
    <text class="slot-talk" x="1662" y="1401">Terrell Oakes - Multiple Income Streams / Keystone Track</text>

    <text class="slot-time" x="1662" y="1444">10:00 am</text>
    <text class="slot-talk" x="1662" y="1466">Lorna Beckett - Marketing though Social Media</text>

    <text class="slot-time" x="1662" y="1509">10:45 am</text>
    <text class="slot-talk" x="1662" y="1531">Raul Denning - Generating Business through Kelp-Nest</text>

    <text class="slot-time" x="1662" y="1574">11:30 am</text>
    <text class="slot-talk" x="1662" y="1596">Tunde Adesemi - Real Estate Investing</text>

    <text class="slot-time" x="1662" y="1639">12:15 pm</text>
    <text class="slot-talk" x="1662" y="1661">Marcus Oyelowo - (Main Speaker) Training Topic TBA</text>
  </g>

  <!-- contact -->
  <g class="contact-block">
    <text class="contact" x="270" y="1536">FOR MORE INFORMATION</text>
    <text class="contact" x="270" y="1570">CALL DESMOND PRYCE AT</text>
    <path class="fill-paper" d="M274 1588c2-2 5-2 6 0l3 5c1 2 0 4-1 5l-2 1c1 4 4 7 8 9l1-2c1-1 3-2 5-1l5 3c2 1 2 4 0 6l-2 2c-3 2-8 1-13-3-5-4-9-9-11-14-1-3-1-6 1-8z"/>
    <text class="contact-small" x="300" y="1606">(240) 555-0192 OR</text>
    <rect class="fill-paper" x="272" y="1622" width="21" height="15" rx="1.5"/>
    <polyline points="272,1623 282.5,1631 293,1623" fill="none" stroke="var(--teal)" stroke-width="2"/>
    <text class="contact-small" x="300" y="1638" font-size="22">dpryce@harborsummithomes.example</text>
  </g>
</svg>
</body>
</html>
```